Bref créative
Harbor Building Partners Company Brochure
HBP Brochure
"We Strive to Exceed Our Customers Expectations"
We're looking for a simple, yet unique and eye catching brochure in a unique format (8 1/2" by 8 1/2"). Each side should be 8 ½" x 8 ½" so that when it is open it is 8 ½" x 17"...or other dimensions that are unique and can easily fit in a portfolio case that's normally 9" x 12" maximum). Should have front cover, inside of front cover, inside of back cover, and back cover...a 4-part brochure. Vibrant and colorful, yet attempting to use the colors of our logo (which was designed by MarkCraftStudio more than a year ago)...colors are vibrant red, grey, and black. Want to include a listing of our services, our mission statement, what sets us apart, and contact info. We're thinking that the text should be superimposed over construction photos. So that each of the inside pages are a large, full page photo and the text strategically positioned on each page. Not sure how the front cover should look...but it could quite simply just have our company logo (which includes our name). The back cover could be red...with just simply our website address.
All of these are just selections as I'm no designer...but I want this brochure to convey that Harbor Building is a "solid company", and want those who view this brochure to get feelings that Harbor Building is secure, stable, capable...yet different as we're a newly formed (less than 2 years old) company that goes all out with customer service and commitment to perform above the clients expectations.
We have all the verbiage/text written...but will need it strategically placed and formatted.
Construction
Architects, Owners of Commercial Properties, Real Estate Investment Trusts, Universities, Hospitals, Non-Profit Organizations, Local and Federal Government Agencies…want our card to convey stability, professionalism, high-energy, performance driven…and want the card to catch their eye. Our target of Architects like “flash”…our Investment Trusts, Government entities like strong, confident, stable, no-risk, proven performer.
Don't think I can say more than what I've said. Like I've said before, we're the new firm in a town (Washington, DC) that has a lot of well established construction general contractors. We need something that will catch someone's eye, yet not be frilly or silly, to the point they'll want to read more inside.
Here's our current logo that we love, which was created by MarkCraftStudio

```html
<!DOCTYPE html>
<html lang="en">
<head>
<meta charset="utf-8">
<title>Harbor Building Partners — Brochure Spread</title>
<link href="https://fonts.googleapis.com/css2?family=Arimo:wght@400;700&family=Tinos:wght@400;700&display=swap" rel="stylesheet">
<style>
  :root {
    --brand-red: #c8201f;
    --ink: #2e2e2e;
    --heading-grey: #3c3c3c;
    --paper: #ffffff;
    --blueprint-light: #f3f3f1;
    --blueprint-mid: #e4e4e0;
    --panel-grey: #d9d9d6;
    --photo-dark: #1c1a1d;
    --photo-warm: #8a4a1c;
    --photo-glow: #d98a3a;
    --overlay-text: #f2ece4;
  }
  * { box-sizing: border-box; margin: 0; padding: 0; }
  html, body { width: 1200px; height: 600px; overflow: hidden; background: var(--paper); }
  .spread { position: relative; width: 1200px; height: 600px; display: flex; font-family: "Arimo", Arial, sans-serif; color: var(--ink); }

  .page { position: relative; width: 600px; height: 600px; overflow: hidden; background: var(--paper); }

  .blueprint-wash {
    position: absolute; inset: 0;
    background: linear-gradient(135deg, var(--blueprint-mid) 0%, var(--blueprint-light) 45%, var(--paper) 100%);
    opacity: .8;
  }
  .top-panel { position: absolute; top: 0; right: 0; width: 230px; height: 52px; background: var(--panel-grey); opacity: .7; }

  .brand { position: absolute; top: 16px; left: 14px; }
  .brand-name { font-weight: 700; font-size: 15px; line-height: 1; color: var(--brand-red); white-space: nowrap; }

  .section-title { font-weight: 400; font-size: 22px; line-height: 1; color: var(--heading-grey); margin-bottom: 8px; }
  .column { position: absolute; }
  .column p {
    font-size: 9.6px; line-height: 10.9px; font-weight: 700; text-align: justify; color: var(--ink); margin-bottom: 11px;
  }
  .about { left: 175px; top: 48px; width: 358px; }
  .services { left: 20px; top: 212px; width: 276px; }

  .photo {
    position: absolute; top: 0; right: 0; width: 302px; height: 600px;
    background: linear-gradient(180deg, var(--photo-dark) 0%, var(--photo-warm) 35%, var(--photo-glow) 55%, var(--photo-warm) 72%, var(--photo-dark) 100%);
  }
  .photo-accent { position: absolute; top: 0; right: 0; width: 8px; height: 120px; background: var(--brand-red); }
  .audience {
    position: absolute; left: 302px; top: 392px; width: 298px; height: 208px;
    background: rgba(20, 16, 18, .55); padding: 12px 10px 0 12px;
    font-family: "Tinos", "Times New Roman", serif; color: var(--overlay-text);
  }
  .audience h3 { font-size: 9.5px; font-weight: 700; margin-bottom: 8px; }
  .audience p { font-size: 9.5px; line-height: 12px; }
</style>
</head>
<body>
<div class="spread">
  <section class="page page-left">
    <div class="blueprint-wash" role="img" aria-label="Faint architectural floor plan drawing in light grey"></div>
    <div class="top-panel"></div>
    <div class="brand">
      <span class="brand-name">Harbor Building Partners</span>
    </div>
    <div class="column about">
      <h2 class="section-title">About Us</h2>
      <p>Please provide your content.Text:We're looking for a simple, yet unique and eye catching brochure in a unique format (8 1/2" by 8 1/2"). Each side should be 8 ½" x 8 ½" so that when it is open it is 8 ½" x 17"...or other dimensions that are unique and can easily fit in a portfolio case that's normally 9" x 12" maximum). Should have front cover, inside of front cover, inside of back cover, and back cover...a 4-part brochure. Vibrant and colorful, yet attempting to use the colors of our logo (which was designed by MarkCraftStudio more than a year ago)...colors are vibrant red, grey, and black. Want to include a listing of our services, our mission statement, what sets us apart, and contact info. We're thinking that the text should be superimposed over construction photos. So that each of the inside pages are a large, full page photo and the text strategically positioned on each page. Not sure how the front cover should look...but it could quite simply just have our company logo (which includes our name). The back cover could be red...with just simply our website address.</p>
      <p>All of these are just selections as I'm no designer...but I want this brochure to convey that Harbor Building is a "solid company", and want those who view this brochure to get feelings that Harbor Building is secure, stable, capable...yet different as we're a newly formed (less than 2 years old) company that goes all out with customer service and commitment to perform above the clients expectations. We have all the verbiage/text written...but will need it strategically placed and formatted.</p>
    </div>
  </section>

  <section class="page page-right">
    <div class="column services">
      <h2 class="section-title">Our Services</h2>
      <p>Please provide your content.Text:We're looking for a simple, yet unique and eye catching brochure in a unique format (8 1/2" by 8 1/2"). Each side should be 8 ½" x 8 ½" so that when it is open it is 8 ½" x 17"...or other dimensions that are unique and can easily fit in a portfolio case that's normally 9" x 12" maximum). Should have front cover, inside of front cover, inside of back cover, and back cover...a 4-part brochure. Vibrant and colorful, yet attempting to use the colors of our logo (which was designed by MarkCraftStudio more than a year ago)...colors are vibrant red, grey, and black. Want to include a listing of our services, our mission statement, what sets us apart, and contact info. We're thinking that the text should be superimposed over construction photos. So that each of the inside pages are a large, full page photo and the text strategically positioned on each page. Not sure how the front cover should look...but it could quite simply just have our company logo (which includes our name). The back cover could be red...with just simply our website address.</p>
    </div>
    <div class="photo" role="img" aria-label="Photo of a modern office building lit warm orange at dusk"></div>
    <div class="photo-accent"></div>
    <div class="audience">
      <h3>Target audience (Corporate, Fun, Personal)</h3>
      <p>Architects, Owners of Commercial Properties, Real Estate Investment Trusts, Universities, Hospitals, Non-Profit Organizations, Local and Federal Government Agencies…want our card to convey stability, professionalism, high-energy, performance driven…and want the card to catch their eye. Our target of Architects like “flash”…our Investment Trusts, Government entities like strong, confident, stable, no-risk, proven performer.</p>
    </div>
  </section>
</div>
</body>
</html>
```